Quorvin Upcoming Gigs

One page graphic with my upcoming dates. Logo and photo attached, and sample from last flyer. Text:

QUORVIN

UPCOMING DATES

3/26/18 Tidal Plums (Las Vegas, NV)

4/1/18 Venture Hollow 2847 M St (Sac, CA)

4/8/18 Amber Heron (Sac, CA)

5/5/18 Low Ceiling @ Silver Moth (Sac, CA)

5/10/18 Pellman Art Museum (Sac, CA)

5/11/18 Vif Brume @ Cafe du Lierre (Sac, CA)

5/27/18 Sonnlicht JTR @ Vox (Sac, CA)

Save The Date: 9/21/18 Lanterns Festival (Puerto Nuevo, MX)

plazabook.example/quorvin482

Target Market(s)

House/Electronic Music

Industry/Entity Type

Night Club

Font styles to use
Sans Serif

Colors

Designer to choose colors to be used in the design.

Requirements
Must have
• Quorvin logo or something that looks good instead. Prefer photo to be in but not necessary.
Nice to have

```html
<!DOCTYPE html>
<html lang="en">
<head>
<meta charset="utf-8">
<title>Quorvin – Upcoming Dates</title>
<link rel="stylesheet" href="https://fonts.googleapis.com/css2?family=Roboto+Condensed:wght@700&display=swap">
<style>
  :root {
    --bg-deep: #0d1a2e;
    --bg-mid: #15304a;
    --bg-teal: #3f9a86;
    --logo-blue: #2f7fe8;
    --head-light: #7fd0ff;
    --head-dark: #1f5fe0;
    --date-orange: #f4a03a;
    --venue-pale: #dccbf2;
    --venue-violet: #8c7ce6;
    --venue-blue: #3d5fe6;
    --link-pale: #d7d4f5;
  }
  * { box-sizing: border-box; margin: 0; padding: 0; }
  html, body { width: 1200px; height: 1200px; overflow: hidden; background: var(--bg-deep); }
  .flyer {
    position: relative;
    width: 1200px;
    height: 1200px;
    overflow: hidden;
    font-family: "Roboto Condensed", "Arial Narrow", sans-serif;
    font-weight: 700;
    background:
      radial-gradient(ellipse 70% 45% at 50% 0%, rgba(63,154,134,0.85), rgba(63,154,134,0) 70%),
      radial-gradient(ellipse 60% 55% at 50% 50%, var(--bg-mid), var(--bg-deep) 80%);
  }
  .performer-photo {
    position: absolute;
    left: 120px;
    top: 230px;
    width: 1080px;
    height: 500px;
    background:
      radial-gradient(ellipse 30% 40% at 45% 40%, rgba(240,110,140,0.75), rgba(240,110,140,0) 70%),
      radial-gradient(ellipse 55% 60% at 40% 35%, rgba(50,70,220,0.85), rgba(50,70,220,0) 75%),
      linear-gradient(170deg, rgba(80,180,220,0) 60%, rgba(110,170,220,0.45) 80%, rgba(200,60,110,0.35) 95%);
    border-radius: 40px;
    filter: blur(2px);
  }
  .logo-name {
    position: absolute;
    left: 0;
    top: 52px;
    width: 1200px;
    text-align: center;
    font-size: 168px;
    line-height: 1;
    letter-spacing: 18px;
    color: var(--logo-blue);
  }
  .section-title {
    position: absolute;
    left: 232px;
    top: 566px;
    font-size: 86px;
    line-height: 1;
    transform: scaleX(0.78);
    transform-origin: left center;
    white-space: nowrap;
    background: linear-gradient(180deg, var(--head-light), var(--head-dark));
    -webkit-background-clip: text;
    background-clip: text;
    color: transparent;
  }
  .gig-list { position: absolute; left: 0; top: 684px; width: 1200px; list-style: none; }
  .gig {
    position: relative;
    height: 51px;
    font-size: 33px;
    line-height: 51px;
    white-space: nowrap;
  }
  .gig span { position: absolute; top: 0; }
  .gig-date { left: 180px; color: var(--date-orange); }
  .gig-venue { left: 338px; transform: scaleX(0.86); transform-origin: left center; }
  .gig-place { left: 770px; color: var(--date-orange); transform: scaleX(0.86); transform-origin: left center; }
  .venue-pale { color: var(--venue-pale); }
  .venue-violet { color: var(--venue-violet); }
  .venue-blue { color: var(--venue-blue); }
  .save-date {
    position: absolute;
    left: 64px;
    top: 1048px;
    font-size: 33px;
    white-space: nowrap;
    color: var(--date-orange);
    transform: scaleX(0.88);
    transform-origin: left center;
  }
  .save-date .fest-name { color: var(--venue-violet); margin: 0 12px; }
  .social-link {
    position: absolute;
    left: 66px;
    top: 1100px;
    font-size: 32px;
    color: var(--link-pale);
    transform: scaleX(0.88);
    transform-origin: left center;
    white-space: nowrap;
  }
</style>
</head>
<body>
<main class="flyer">
  <div class="performer-photo" role="img" aria-label="Photo of the DJ performing behind the decks under blue and pink club lights"></div>

  <h1 class="logo-name">QUORVIN</h1>

  <h2 class="section-title">UPCOMING DATES</h2>

  <ul class="gig-list">
    <li class="gig"><span class="gig-date">3/26/18</span><span class="gig-venue venue-pale">TIDAL PLUMS</span><span class="gig-place">(LAS VEGAS, NV)</span></li>
    <li class="gig"><span class="gig-date">4/1/18</span><span class="gig-venue venue-pale">VENTURE HOLLOW 2847 M ST</span><span class="gig-place">(SAC, CA)</span></li>
    <li class="gig"><span class="gig-date">4/8/18</span><span class="gig-venue venue-pale">AMBER HERON</span><span class="gig-place">(SAC, CA)</span></li>
    <li class="gig"><span class="gig-date">5/5/18</span><span class="gig-venue venue-violet">LOW CEILING @ SILVER MOTH</span><span class="gig-place">(SAC, CA)</span></li>
    <li class="gig"><span class="gig-date">5/10/18</span><span class="gig-venue venue-blue">PELLMAN ART MUSEUM</span><span class="gig-place">(SAC, CA)</span></li>
    <li class="gig"><span class="gig-date">5/11/18</span><span class="gig-venue venue-blue">VIF BRUME @ CAFE DU LIERRE</span><span class="gig-place">(SAC, CA)</span></li>
    <li class="gig"><span class="gig-date">5/27/18</span><span class="gig-venue venue-blue">SONNLICHT JTR @ VOX</span><span class="gig-place">(SAC, CA)</span></li>
  </ul>

  <p class="save-date">SAVE THE DATE: 9/21/18 <span class="fest-name">LANTERNS FESTIVAL</span>(PUERTO NUEVO, MX)</p>

  <p class="social-link">PLAZABOOK.EXAMPLE/QUORVIN482</p>
</main>
</body>
</html>
```